Kestro Vale - Dog Supplement Brand

Here a link to a word doc with all of my info.
Please read it carefully.
https://files.brindlepad.net/sheet/7QwLx2mTa8Rk3PzNv0eYc5Hj9UfGs46Bd1Oi-Lp-3/view?ref=shared
Its 2 pages. Home Page and Product Page.
Oh and btw: the poses I attached dont have a shadow, so it would be good if you added a shadow to the poses .
If you have any questions please let me know.
Target Market(s)
Dog Owners In UK
Industry/Entity Type
Dog supplements
Number of Pages Required
2 page
Requirements
Must have
- Home page and product page files. Super Hero Theme.

```html
<!DOCTYPE html>
<html lang="en">
<head>
<meta charset="utf-8">
<title>Kestro Vale – Home</title>
<link rel="stylesheet" href="https://fonts.googleapis.com/css2?family=Poppins:wght@400;500;600;700;800&display=swap">
<style>
:root{
  --red:#d4121d;
  --red-dark:#a80d15;
  --blue:#4b9be6;
  --black:#0c0c0c;
  --ink:#1b1b1b;
  --muted:#666a70;
  --grey:#eef0f3;
  --white:#ffffff;
  --pink:#f6dfe6;
}
*{box-sizing:border-box;margin:0;padding:0}
html,body{width:1200px;height:4892px;overflow:hidden}
body{position:relative;font-family:"Poppins",Arial,sans-serif;color:var(--ink);background:var(--white)}
.abs{position:absolute}
.btn{display:inline-block;border-radius:30px;font-weight:600;color:var(--white);text-decoration:none;white-space:nowrap}
.btn-red{background:var(--red);box-shadow:0 6px 14px rgba(212,18,29,.35)}
.btn-black{background:var(--black)}
.body-copy{font-size:14px;line-height:1.75;color:var(--muted)}
.placeholder{border-radius:24px}

/* announcement + header */
.announcement{top:0;left:0;width:1200px;height:24px;background:var(--red);color:var(--white);font-size:11px;text-align:center;line-height:24px}
.site-header{top:24px;left:0;width:1200px;height:56px;background:var(--white)}
.menu-icon{left:34px;top:20px;width:18px;height:14px;border-top:2px solid var(--ink);border-bottom:2px solid var(--ink)}
.menu-icon::after{content:"";position:absolute;left:0;top:4px;width:18px;height:2px;background:var(--ink)}
.brand{left:0;width:1200px;top:15px;text-align:center}
.brand span{display:inline-block;font-weight:800;font-size:16px;color:var(--ink);letter-spacing:.5px}
.brand span::before{content:"";display:inline-block;width:14px;height:14px;background:var(--red);border-radius:50%;margin-right:7px;vertical-align:-1px}
.header-icons{right:34px;top:18px;display:flex;gap:16px}

/* hero */
.hero{top:80px;left:0;width:1200px;height:580px}
.hero-character{left:150px;top:10px;width:300px;height:560px;border-radius:140px 140px 60px 60px;background:linear-gradient(160deg,#f1f1f1 0%,#9aa0a8 45%,var(--red) 100%)}
.hero-title{left:650px;top:188px;width:420px;font-size:33px;font-weight:700;line-height:1.3;color:var(--white)}
.hero .btn{left:650px;top:380px;padding:9px 26px;font-size:12px}

/* about */
.about-title{left:120px;top:760px;font-size:48px;font-weight:800;line-height:1.1;letter-spacing:.5px}
.about-title em{font-style:normal;color:var(--red)}
.about-copy{left:120px;top:900px;width:560px}
.about-copy p+p{margin-top:18px}
.about .btn{left:120px;top:1222px;padding:15px 32px;font-size:14px}
.about-circle{left:760px;top:750px;width:270px;height:270px;border-radius:50%;background:var(--pink)}
.about-character{left:720px;top:760px;width:300px;height:320px;border-radius:120px;background:linear-gradient(170deg,#eaeaea,#8d939b 55%,var(--red))}

/* offer */
.offer-bg{top:1300px;left:0;width:1200px;height:1040px}
.offer-character{left:540px;top:1260px;width:120px;height:170px;border-radius:50px;background:linear-gradient(170deg,#e9e9e9,#8d939b 60%,var(--red))}
.offer-title{left:0;width:1200px;top:1490px;text-align:center;color:var(--white);font-size:40px;font-weight:800;letter-spacing:1px}
.product-card{width:310px;height:310px;border-radius:50%;overflow:hidden;border:4px solid var(--white)}
.product-photo{position:absolute;inset:0}
.product-band{position:absolute;left:0;right:0;bottom:0;height:120px;color:var(--white);text-align:center;padding-top:28px;font-size:14px;font-weight:700;line-height:1.35}
.product-band small{display:block;font-weight:500;font-size:13px}
.band-blue{background:var(--blue)}
.band-red{background:var(--red)}
.band-green{background:#18a34a}
.band-orange{background:#f5a10d}
.band-purple{background:#8a22d6}
.band-brown{background:#5a3418}

/* video */
.red-band{top:2560px;left:0;width:1200px;height:720px}
.video{left:220px;top:2300px;width:870px;height:430px;border-radius:26px;overflow:hidden;background:linear-gradient(160deg,#2f4a1f,#a07a3a 45%,#d6a95b 60%,#3e5a26);box-shadow:0 14px 30px rgba(0,0,0,.25)}
.play{left:620px;top:2480px;width:70px;height:70px;border-radius:50%;background:rgba(255,255,255,.9)}
.play::after{content:"";position:absolute;left:27px;top:21px;border-left:22px solid var(--ink);border-top:14px solid transparent;border-bottom:14px solid transparent}
.video-character{left:1000px;top:2450px;width:160px;height:290px;border-radius:70px;background:linear-gradient(170deg,#ececec,#8d939b 55%,var(--red))}

/* testimonials */
.love-title{left:0;width:1200px;top:2762px;text-align:center;color:var(--white);font-size:40px;font-weight:800;letter-spacing:1px;line-height:1.2}
.review{top:2850px;width:272px;height:350px;background:var(--white);border-radius:14px;padding:24px 22px;box-shadow:0 10px 24px rgba(0,0,0,.2)}
.review .body-copy{font-size:12.5px;line-height:1.7}
.review-name{position:absolute;left:22px;bottom:28px;font-weight:700;font-size:15px}
.review-name small{display:block;font-weight:400;font-size:11px;color:var(--muted)}
.quote{position:absolute;right:22px;bottom:28px;font-size:48px;font-weight:800;color:var(--red);line-height:30px;height:30px}
.arrow{top:3080px;width:30px;height:30px;border-radius:50%;background:var(--white);color:var(--red);font-size:16px;font-weight:700;text-align:center;line-height:30px}

/* certified */
.cert-circle{left:110px;top:3340px;width:420px;height:420px;border-radius:50%;background:var(--red)}
.cert-character{left:150px;top:3310px;width:340px;height:510px;border-radius:130px;background:linear-gradient(170deg,#f2f2f2,#a5abb2 55%,#2fbf4a)}
.cert-title{left:600px;top:3380px;font-size:40px;font-weight:800;line-height:1.2}
.cert-title em{font-style:normal;color:var(--red)}
.cert-copy{left:600px;top:3500px;width:470px;font-size:13.5px}
.badges{left:600px;top:3690px;display:flex;gap:14px}
.badge{width:48px;height:48px;border-radius:50%;border:3px solid #c9ccd0;background:var(--white)}
.badge:nth-child(2){border-color:#2fbf4a;background:#e6f7ea}

/* why */
.why-bg{top:3860px;left:0;width:1200px;height:580px;background:var(--grey)}
.why-title{left:0;width:1200px;top:3950px;text-align:center;color:var(--red);font-size:40px;font-weight:800;letter-spacing:1px}
.features{left:110px;top:4060px;width:980px;display:flex;justify-content:space-between}
.feature{width:170px;text-align:center;font-size:14px;font-weight:500;line-height:1.45}
.feature svg{display:block;margin:0 auto 14px}
.dots{left:0;width:1200px;top:4290px;display:flex;justify-content:center;gap:7px}
.dots i{width:12px;height:12px;border-radius:50%;border:2px solid var(--red)}
.dots i:first-child{background:var(--red)}

/* cta */
.cta{top:4440px;left:0;width:1200px;height:250px;background:var(--red)}
.cta-title{left:0;width:1200px;top:4510px;text-align:center;color:var(--white);font-size:40px;font-weight:800;letter-spacing:1px}
.cta .btn{position:absolute;left:475px;top:145px;width:250px;text-align:center;padding:15px 0;font-size:16px}
.cta-character{left:20px;top:4420px;width:150px;height:300px;border-radius:60px;background:linear-gradient(170deg,#eeeeee,#8d939b 55%,var(--red-dark))}

/* footer */
.footer-label{left:40px;top:4755px;font-size:10px;color:var(--muted)}
.currency{left:40px;top:4772px;width:150px;height:24px;border:1px solid #c4c7cb;border-radius:3px;font-size:10px;line-height:22px;padding-left:6px;white-space:nowrap;overflow:hidden}
.payments{right:40px;top:4776px;display:flex;gap:6px}
.payments i{width:34px;height:22px;border-radius:3px;background:#dfe2e6}
.copyright{right:40px;top:4850px;font-size:10px;color:var(--muted)}
</style>
</head>
<body>

<div class="abs announcement">Free UK delivery on orders over £30 · Join the squad today</div>
<header class="abs site-header">
  <div class="abs menu-icon"></div>
  <div class="abs brand"><span>KESTRO VALE</span></div>
  <div class="abs header-icons">
    <svg width="16" height="16" viewBox="0 0 16 16" fill="none" stroke="#1b1b1b" stroke-width="2"><circle cx="7" cy="7" r="5"/><path d="M11 11l4 4"/></svg>
    <svg width="16" height="16" viewBox="0 0 16 16" fill="none" stroke="#1b1b1b" stroke-width="2"><circle cx="8" cy="5" r="3"/><path d="M2 15c0-4 12-4 12 0"/></svg>
    <svg width="16" height="16" viewBox="0 0 16 16" fill="none" stroke="#1b1b1b" stroke-width="2"><path d="M2 5h12l-1 10H3z"/><path d="M5 5a3 3 0 016 0"/></svg>
  </div>
</header>

<section class="abs hero">
  <svg class="abs" style="left:0;top:0" width="1200" height="580" viewBox="0 0 1200 580">
    <rect width="1200" height="520" fill="#4b9be6"/>
    <path d="M0 500 C300 560 600 470 900 510 C1030 528 1120 520 1200 500 V580 H0Z" fill="#d4121d"/>
    <path d="M0 520 C300 580 600 495 900 530 C1030 545 1120 540 1200 520 V580 H0Z" fill="#ffffff"/>
    <path d="M0 490 C300 550 600 460 900 500 C1030 518 1120 510 1200 490 V502 C1120 522 1030 530 900 512 C600 472 300 562 0 502Z" fill="#4b9be6"/>
  </svg>
  <div class="abs hero-character placeholder" role="img" aria-label="Kestro Vale superhero dog mascot in red cape, flying pose with shadow"></div>
  <h1 class="abs hero-title">Join Forces With Kestro Vale &amp; Let Him Be Your Beloved Dog's Hero!</h1>
  <a class="abs btn btn-red" href="#">● JOIN FORCES</a>
</section>

<section class="about">
  <h2 class="abs about-title">HI! I'M KESTRO<br><em>VALE</em></h2>
  <div class="abs about-copy body-copy">
    <p>Lorem ipsum dolor sit amet, consectetur adipiscing elit, sed do eiusmod tempor incididunt ut labore et dolore magna aliqua. Ut enim ad minim veniam, quis nostrud exercitation ullamco laboris nisi ut aliquip ex ea commodo consequat. Duis aute irure dolor in reprehenderit in voluptate velit esse cillum dolore eu fugiat nulla pariatur. Excepteur sint occaecat cupidatat non proident, sunt in culpa qui officia deserunt mollit anim id est laborum.</p>
    <p>Lorem ipsum dolor sit amet, consectetur adipiscing elit, sed do eiusmod tempor incididunt ut labore et dolore magna aliqua. Ut enim ad minim veniam, quis nostrud exercitation.</p>
  </div>
  <a class="abs btn btn-red" href="#">Read More About Me</a>
  <div class="abs about-circle"></div>
  <div class="abs about-character placeholder" role="img" aria-label="Kestro Vale mascot flexing arm, with shadow"></div>
</section>

<section class="offer">
  <svg class="abs offer-bg" width="1200" height="1040" viewBox="0 0 1200 1040">
    <path d="M0 110 C250 40 420 20 600 70 C800 125 1000 30 1200 0 V1040 H0Z" fill="#0c0c0c"/>
  </svg>
  <div class="abs offer-character" role="img" aria-label="Kestro Vale mascot standing, arms crossed"></div>
  <h2 class="abs offer-title">HERE'S WHAT I OFFER</h2>

  <div class="abs product-card" style="left:120px;top:1570px">
    <div class="product-photo" role="img" aria-label="Photo of a calm small dog resting" style="background:linear-gradient(160deg,#6b4a2e,#c9a27a 55%,#3b2a1c)"></div>
    <div class="product-band band-blue">KESTRO VALE<small>Calm</small></div>
  </div>
  <div class="abs product-card" style="left:445px;top:1570px">
    <div class="product-photo" role="img" aria-label="Photo of two dogs playing outdoors" style="background:linear-gradient(160deg,#7a5b2a,#d3a86a 55%,#6b7a3a)"></div>
    <div class="product-band band-red">KESTRO VALE<small>Joint Support</small></div>
  </div>
  <div class="abs product-card" style="left:770px;top:1570px">
    <div class="product-photo" role="img" aria-label="Multivits supplement tub product shot" style="background:linear-gradient(160deg,#1f8a3f,#9fd2a7 50%,#1f8a3f)"></div>
    <div class="product-band band-green">KESTRO VALE<small>Multivits</small><small>$120.00</small></div>
  </div>

  <div class="abs product-card" style="left:120px;top:1905px">
    <div class="product-photo" role="img" aria-label="Photo of a terrier in grass" style="background:linear-gradient(160deg,#7e9a5a,#d9c3a0 55%,#a86a3a)"></div>
    <div class="product-band band-orange">KESTRO VALE<small>Omega 3/6</small></div>
  </div>
  <div class="abs product-card" style="left:445px;top:1905px">
    <div class="product-photo" role="img" aria-label="Photo of a red setter sitting" style="background:linear-gradient(160deg,#5e7a3a,#a5502a 55%,#6b3a1e)"></div>
    <div class="product-band band-purple">KESTRO VALE<small>Probiotics</small></div>
  </div>
  <div class="abs product-card" style="left:770px;top:1905px">
    <div class="product-photo" role="img" aria-label="Photo of a brown bully dog" style="background:linear-gradient(160deg,#d7d2cc,#7a4a2e 55%,#3a2416)"></div>
    <div class="product-band band-brown">KESTRO VALE<small>Digestive Support</small></div>
  </div>
</section>

<section class="video-block">
  <svg class="abs red-band" width="1200" height="720" viewBox="0 0 1200 720">
    <path d="M0 60 L1200 0 V720 H0Z" fill="#d4121d"/>
  </svg>
  <div class="abs video" role="img" aria-label="Video still of a golden retriever lying in a sunny field"></div>
  <div class="abs play"></div>
  <div class="abs video-character" role="img" aria-label="Kestro Vale mascot standing with cape"></div>
</section>

<section class="reviews">
  <h2 class="abs love-title">PEOPLE LOVE ME</h2>
  <div class="abs arrow" style="left:70px">‹</div>
  <div class="abs arrow" style="left:1100px">›</div>
  <article class="abs review" style="left:240px">
    <p class="body-copy">Lorem ipsum dolor sit amet, consectetur adipiscing elit, sed do eiusmod tempor incididunt ut labore et dolore magna aliqua. Ut enim ad minim veniam, quis nostrud exercitation ullamco laboris nisi ut aliquip ex ea commodo. Duis aute irure dolor in reprehenderit in voluptate velit esse.</p>
    <div class="review-name">Dara Whitcombe<small>Lorem ipsum dolor sit</small></div>
    <div class="quote">“</div>
  </article>
  <article class="abs review" style="left:534px">
    <p class="body-copy">Lorem ipsum dolor sit amet, consectetur adipiscing elit, sed do eiusmod tempor incididunt ut labore et dolore magna aliqua. Ut enim ad minim veniam, quis nostrud exercitation ullamco laboris nisi ut aliquip ex ea commodo. Duis aute irure dolor in reprehenderit in voluptate velit esse.</p>
    <div class="review-name">Dara Whitcombe<small>Lorem ipsum dolor sit</small></div>
    <div class="quote">“</div>
  </article>
  <article class="abs review" style="left:828px">
    <p class="body-copy">Lorem ipsum dolor sit amet, consectetur adipiscing elit, sed do eiusmod tempor incididunt ut labore et dolore magna aliqua. Ut enim ad minim veniam, quis nostrud exercitation ullamco laboris nisi ut aliquip ex ea commodo. Duis aute irure dolor in reprehenderit in voluptate velit esse.</p>
    <div class="review-name">Dara Whitcombe<small>Lorem ipsum dolor sit</small></div>
    <div class="quote">“</div>
  </article>
</section>

<section class="certified">
  <div class="abs cert-circle"></div>
  <div class="abs cert-character placeholder" role="img" aria-label="Kestro Vale mascot in lab coat holding a green test tube"></div>
  <h2 class="abs cert-title">REGULATED &amp;<br><em>CERTIFIED</em></h2>
  <p class="abs cert-copy body-copy">Lorem ipsum dolor sit amet, consectetur adipiscing elit, sed do eiusmod tempor incididunt ut labore et dolore magna aliqua. Ut enim ad minim veniam, quis nostrud exercitation ullamco laboris nisi ut aliquip ex ea commodo consequat. Duis aute irure dolor in reprehenderit in voluptate velit esse cillum dolore eu fugiat nulla pariatur. Excepteur sint occaecat cupidatat non proident, sunt in culpa qui officia deserunt mollit anim id est laborum.</p>
  <div class="abs badges"><i class="badge"></i><i class="badge"></i><i class="badge"></i></div>
</section>

<section class="why">
  <div class="abs why-bg"></div>
  <h2 class="abs why-title">WHY CHOOSE ME?</h2>
  <div class="abs features">
    <div class="feature">
      <svg width="44" height="44" viewBox="0 0 44 44" fill="none" stroke="#d4121d" stroke-width="2.5"><path d="M22 40V18"/><path d="M22 24c-8 0-12-6-12-14 8 0 12 6 12 14z"/><path d="M22 20c0-8 4-14 12-14 0 8-4 14-12 14z"/></svg>
      Only Organic &amp;<br>Natural Ingredients
    </div>
    <div class="feature">
      <svg width="44" height="44" viewBox="0 0 44 44" fill="none" stroke="#d4121d" stroke-width="2.5"><rect x="3" y="12" width="24" height="18"/><path d="M27 18h8l6 6v6H27z"/><circle cx="11" cy="33" r="3"/><circle cx="34" cy="33" r="3"/></svg>
      Free Next Day<br>UK Delivery
    </div>
    <div class="feature">
      <svg width="44" height="44" viewBox="0 0 44 44" fill="none" stroke="#d4121d" stroke-width="2.5"><circle cx="22" cy="14" r="8"/><path d="M7 40c0-10 30-10 30 0"/></svg>
      33% OFF For All<br>Kestro Vale Squad<br>Members
    </div>
    <div class="feature">
      <svg width="44" height="44" viewBox="0 0 44 44" fill="none" stroke="#d4121d" stroke-width="2.5"><circle cx="22" cy="22" r="18"/><circle cx="22" cy="22" r="11"/><path d="M17 22l4 4 7-8"/></svg>
      Regulated and<br>Certified
    </div>
    <div class="feature">
      <svg width="44" height="44" viewBox="0 0 44 44" fill="none" stroke="#d4121d" stroke-width="2.5"><path d="M22 38S5 27 5 16a8.5 8.5 0 0117-3 8.5 8.5 0 0117 3c0 11-17 22-17 22z"/></svg>
      10% Charity<br>Donation
    </div>
  </div>
  <div class="abs dots"><i></i><i></i><i></i><i></i></div>
</section>

<section class="abs cta">
  <a class="btn btn-black" href="#">JOIN FORCES!</a>
</section>
<h2 class="abs cta-title">HOW ABOUT YOU GIVE IT A TRY?</h2>
<div class="abs cta-character" role="img" aria-label="Kestro Vale mascot waving, with shadow"></div>

<footer>
  <div class="abs footer-label">Country/region</div>
  <div class="abs currency">United Kingdom (GBP £) ▾</div>
  <div class="abs payments"><i></i><i></i><i></i><i></i><i></i><i></i><i></i><i></i></div>
  <div class="abs copyright">© 2024 Kestro Vale</div>
</footer>

</body>
</html>
```